Wellness bold & beautiful PowerPoint Template

I will like a PowerPoint template, matching my brand, designed for my business.
- Some words that describe our brand identity are: wellness, natural, calming, simplicity, clean
- For icons, we prefer line icons.
- Website: http://www.verindale.com/
- PowerPoint board: https://www.pinterest.com/tobramelke/verindale-powerpoint/
- Branding board: https://www.pinterest.com/tobramelke/verindale-branding/
FYI: I am attaching a rough draft of a powerpoint presentation we are preparing
Target Market(s)
Women 23-48 interested in wellness
Industry/Entity Type
Health And Wellness
Font styles to use
Other font styles liked:
- Open Sans, Helvitica, Meddon
Requirements
Must have
- cover page, about page, author page, table of content, table format, graph format, list format, 2 column template.
Nice to have
- time line page sample

```html
<!DOCTYPE html>
<html lang="en">
<head>
<meta charset="utf-8">
<title>Verindale – Unclutter Your Space template</title>
<link href="https://fonts.googleapis.com/css2?family=Open+Sans:wght@400;600;700&family=Alfa+Slab+One&family=Roboto+Slab:wght@400;700&display=swap" rel="stylesheet">
<style>
:root{
  --board:#6b6b6b;
  --paper:#ffffff;
  --green:#8cc63f;
  --green-dark:#6fa82a;
  --plum:#b8549c;
  --plum-light:#e9d6e6;
  --ink:#333333;
  --muted:#777777;
  --chart-dark:#3a3a3a;
  --chart-grey:#8a8a8a;
  --band:#d4d6d4;
}
*{box-sizing:border-box;margin:0;padding:0}
html,body{width:1200px;height:887px;overflow:hidden}
body{background:var(--board);font-family:"Open Sans",Arial,sans-serif;color:var(--ink);position:relative}
.slide{position:absolute;background:var(--paper);overflow:hidden}
.slide-title{position:absolute;left:30px;top:14px;font-size:12.5px;font-weight:400;letter-spacing:.2px;color:#222}
.footer-url{position:absolute;bottom:8px;left:0;right:0;text-align:center;font-size:5px;color:var(--muted)}
.page-no{position:absolute;right:10px;bottom:6px;width:13px;height:13px;border-radius:50%;background:var(--plum);color:#fff;font-size:5px;display:flex;align-items:center;justify-content:center}
.brand{position:absolute;left:12px;bottom:8px;display:flex;align-items:center;gap:3px;font-size:6px;font-weight:600;color:var(--green)}
.brand i{display:block;width:8px;height:8px;border-radius:50%;background:var(--green)}
.photo{position:absolute}

/* cover */
.cover{left:22px;top:14px;width:370px;height:207px}
.cover .photo{inset:0;background:radial-gradient(circle at 75% 30%,#fff6d9 0%,#f4d9a8 25%,#c9cf9a 55%,#7db6a8 100%)}
.cover .brand-cover{position:absolute;left:40px;top:52px;display:flex;align-items:center;gap:4px;font-size:12px;font-weight:600;color:var(--plum)}
.cover .brand-cover i{display:block;width:12px;height:12px;border-radius:50%;background:var(--plum)}
.cover h1{position:absolute;left:30px;top:90px;font-family:"Alfa Slab One",Georgia,serif;font-weight:400;font-size:22px;line-height:1.1;color:#3c3c3c}
.cover .authors{position:absolute;left:32px;top:158px;font-size:5.5px;line-height:1.9;font-weight:600;color:#3c3c3c}
.cover .site{position:absolute;left:32px;bottom:6px;font-size:5px;color:#fff}

/* agenda */
.agenda{left:404px;top:12px;width:375px;height:209px}
.agenda h2{position:absolute;left:30px;top:14px;font-size:12px;font-weight:400}
.agenda ul{position:absolute;list-style:none;font-size:6.2px;line-height:11.2px}
.agenda li::before{content:"";display:inline-block;width:3px;height:3px;background:var(--plum);margin:0 8px 1px 0}
.agenda li.sub{padding-left:12px}
.agenda li.sub::before{width:2px;height:2px}
.agenda .col-a{left:32px;top:48px}
.agenda .col-b{left:200px;top:48px}
.agenda .brand{left:22px}

/* about */
.about{left:795px;top:12px;width:386px;height:209px;background:var(--green)}
.about .brand-about{position:absolute;left:50px;top:96px;display:flex;align-items:center;gap:3px;font-size:7px;font-weight:600;color:#fff}
.about .brand-about i{display:block;width:8px;height:8px;border-radius:50%;background:#fff}
.about h2{position:absolute;left:44px;top:126px;font-size:11px;font-weight:400;color:#222}
.about .photo{left:150px;top:0;width:236px;height:209px;background:linear-gradient(180deg,#4f8fd0 0%,#a9cdeb 45%,#c8c2a0 62%,#8c8f6c 100%)}
.about blockquote{position:absolute;left:160px;top:134px;width:220px;text-align:center;font-family:"Roboto Slab",Georgia,serif;font-size:10px;font-weight:700;color:#fff;line-height:1.15}
.about .about-lead{position:absolute;left:160px;top:172px;width:220px;text-align:center;font-family:"Roboto Slab",Georgia,serif;font-size:7.5px;color:#fff;line-height:1.7}

/* row 2 */
.steps{left:22px;top:233px;width:370px;height:207px}
.steps .item{position:absolute;left:146px;width:200px;font-size:6.2px;line-height:9px}
.steps .item b{display:block;color:var(--plum);font-weight:600}

.timeline{left:404px;top:233px;width:375px;height:207px}
.timeline .stop{position:absolute;top:92px;width:70px;font-size:3.8px;line-height:5px}
.timeline .stop ul{list-style:none}
.timeline .stop li::before{content:"➢ "}

.ladder{left:795px;top:231px;width:386px;height:215px}
.ladder .box{position:absolute;width:108px;height:24px;color:#fff;font-size:5px;line-height:6px;text-align:center;padding:3px 6px}
.ladder .tab{position:absolute;width:20px;height:20px;color:#fff;font-size:8px;display:flex;align-items:center;justify-content:center}

/* row 3 */
.table-slide{left:22px;top:452px;width:370px;height:206px}
.table-slide table{position:absolute;left:70px;top:38px;width:224px;border-collapse:collapse;font-size:5px}
.table-slide td{height:10.2px;padding-left:30px;border:1px solid #fff;color:#222}
.table-slide tr:nth-child(odd) td{background:var(--plum-light)}
.table-slide tr:nth-child(even) td{background:var(--green);color:#fff}

.team{left:407px;top:449px;width:370px;height:207px}
.team .member{position:absolute;top:46px;width:76px;text-align:center}
.team .face{width:30px;height:30px;margin:0 auto;background:linear-gradient(160deg,#e8c4a8,#b88b6c)}
.team h3{margin-top:14px;font-size:5.7px;font-weight:400;line-height:7px}
.team .member:nth-child(odd) h3{color:var(--plum)}
.team .member:nth-child(even) h3{color:var(--green)}
.team p{margin-top:4px;font-size:3.8px;line-height:5px;color:#666}

.chart-slide{left:795px;top:455px;width:378px;height:208px}
.chart-slide .legend{position:absolute;top:134px;width:90px;font-size:5.5px;line-height:7px}
.chart-slide .legend b{display:flex;align-items:center;gap:6px;font-weight:600;margin-bottom:6px}
.chart-slide .legend b i{width:7px;height:7px;display:block}

/* row 4 */
.quotes{left:22px;top:671px;width:366px;height:208px}
.quotes .band{position:absolute;left:0;top:0;width:100%;height:129px;background:var(--green)}
.quotes .slide-title{color:#fff}
.quotes .col{position:absolute;top:60px;width:90px;color:#fff;font-size:4.6px;line-height:6px}
.quotes .col b{display:flex;align-items:center;gap:5px;font-size:6px;margin-bottom:3px}
.quotes .testimonial{position:absolute;top:136px;left:70px;width:230px;text-align:center;font-size:4.8px;line-height:6.5px;font-style:italic}
.quotes .testimonial strong{display:block;font-size:6px;margin-bottom:3px}
.quotes .testimonial span{color:var(--green);font-weight:600}
</style>
</head>
<body>

<!-- Cover -->
<section class="slide cover">
  <div class="photo" role="img" aria-label="Sunlit photo of a woman with open arms in a field"></div>
  <div class="brand-cover"><i></i>Verindale</div>
  <h1>UNCLUTTER<br>YOUR SPACE</h1>
  <p class="authors">Tobra Melke @ Verindale<br>Elsa Marlow @ Simply with Elsa</p>
  <p class="site">www.verindale.com</p>
</section>

<!-- Agenda -->
<section class="slide agenda">
  <h2>AGENDA</h2>
  <ul class="col-a">
    <li>Why Unclutter</li><li>The Point of Frustration</li><li>Failed Attempts</li><li>Getting Help</li>
    <li>Steps to creating your best space</li>
    <li class="sub">Declutter</li><li class="sub">Organize</li><li class="sub">Rejuvenate</li><li class="sub">Maintain</li>
    <li>Before &amp; After</li><li>Keeping it real!</li>
  </ul>
  <ul class="col-b">
    <li>Getting Started</li><li>Declutter Action Plan</li><li>Organizational principles – Tips &amp; Tricks</li>
    <li>Feng Shui101</li><li>It's not just the clutter</li><li>Zero Waste Movement</li><li>Getting stuck</li>
    <li class="sub">Online Forum</li><li class="sub">Professional help</li><li>Resources</li>
  </ul>
  <div class="brand"><i></i>Verindale</div>
  <p class="footer-url">www.verindale.com</p>
  <span class="page-no">01</span>
</section>

<!-- About -->
<section class="slide about">
  <div class="brand-about"><i></i>Verindale</div>
  <h2>ABOUT US</h2>
  <div class="photo" role="img" aria-label="Photo of a woman in a sun hat on an open road under a blue sky"></div>
  <blockquote>“SUPPORTING YOUR WELLNESS JOURNEY”</blockquote>
  <p class="about-lead">Helping people live healthier (happier), more balanced and holistic lives</p>
</section>

<!-- Steps list -->
<section class="slide steps">
  <h2 class="slide-title">INSERT YOU SUB TITLE HERE</h2>
  <svg width="140" height="140" viewBox="0 0 140 140" style="position:absolute;left:12px;top:44px">
    <g fill="#8cc63f">
      <polygon points="70,2 130,2 136,12 130,22 70,22"/>
      <polygon points="48,32 130,32 136,42 130,52 48,52"/>
      <polygon points="34,60 130,60 136,70 130,80 34,80"/>
      <polygon points="24,88 130,88 136,98 130,108 24,108"/>
    </g>
    <g fill="#6fa82a">
      <polygon points="70,22 48,32 48,52 70,22"/>
      <polygon points="48,52 34,60 34,80 48,52"/>
      <polygon points="34,80 24,88 24,108 34,80"/>
      <polygon points="24,108 14,118 24,118"/>
    </g>
    <g fill="#fff" font-family="Open Sans,Arial,sans-serif" font-size="9" text-anchor="middle">
      <text x="113" y="15">01</text><text x="113" y="45">02</text><text x="113" y="73">03</text><text x="113" y="101">04</text>
    </g>
  </svg>
  <div class="item" style="top:46px"><b>Insert your text here</b>What we need is a template (or master) which can be varied by ourselves from case to case</div>
  <div class="item" style="top:76px"><b>Insert your text here</b>What we need is a template (or master) which can be varied by ourselves from case to case</div>
  <div class="item" style="top:106px"><b>Insert your text here</b>What we need is a template (or master) which can be varied by ourselves from case to case</div>
  <div class="item" style="top:140px"><b>Insert your text here</b>What we need is a template (or master) which can be varied by ourselves from case to case</div>
  <div class="brand"><i></i>Verindale</div>
  <p class="footer-url">www.verindale.com</p>
  <span class="page-no">01</span>
</section>

<!-- Timeline -->
<section class="slide timeline">
  <h2 class="slide-title">INSERT YOU SUB TITLE HERE</h2>
  <svg width="375" height="90" viewBox="0 0 375 90" style="position:absolute;left:0;top:60px">
    <line x1="20" y1="13" x2="350" y2="13" stroke="#c8c8c8" stroke-width="1"/>
    <g font-family="Open Sans,Arial,sans-serif" font-size="4" fill="#fff" text-anchor="middle">
      <circle cx="48" cy="13" r="5" fill="#8cc63f"/><text x="48" y="14.5">01</text>
      <circle cx="118" cy="13" r="5" fill="#b8549c"/><text x="118" y="14.5">02</text>
      <circle cx="187" cy="13" r="5" fill="#8cc63f"/><text x="187" y="14.5">03</text>
      <circle cx="255" cy="13" r="5" fill="#b8549c"/><text x="255" y="14.5">04</text>
      <circle cx="323" cy="13" r="5" fill="#8cc63f"/><text x="323" y="14.5">05</text>
    </g>
    <g fill="none" stroke="#222" stroke-width="1.2">
      <rect x="43" y="23" width="9" height="9" fill="#222"/>
      <rect x="114" y="23" width="7" height="10" transform="rotate(-12 117 28)"/>
      <circle cx="187" cy="27" r="3.5"/><line x1="187" y1="31" x2="187" y2="34"/>
      <rect x="250" y="23" width="9" height="7" rx="2" fill="#222"/>
      <circle cx="323" cy="27" r="3.5"/><line x1="323" y1="31" x2="323" y2="34"/>
    </g>
  </svg>
  <div class="stop" style="left:24px">Strategy derived from a dynamic optimization problem that maximizes returns within a given risk constraint.</div>
  <div class="stop" style="left:96px">Parameters/assumptions<ul><li>Assume liquid markets</li><li>Assume a price discount/premium on each trade (0-10%)</li></ul></div>
  <div class="stop" style="left:166px">Solution – the optimization problem tells us:<ul><li>When to buy or sell contracts</li><li>Which contracts to buy or sell</li><li>How many contracts to buy or sell</li></ul></div>
  <div class="stop" style="left:240px">We make trades based on these solutions while letting the price discount/premium offered by the market.</div>
  <div class="stop" style="left:304px">Solution – the optimization problem tells us:<ul><li>When to buy or sell contracts</li><li>Which contracts to buy or sell</li><li>How many contracts to buy or sell</li></ul></div>
  <div class="brand"><i></i>Verindale</div>
  <p class="footer-url">www.verindale.com</p>
  <span class="page-no">01</span>
</section>

<!-- Alternating ladder -->
<section class="slide ladder">
  <h2 class="slide-title">INSERT YOU SUB TITLE HERE</h2>
  <div style="position:absolute;left:170px;top:36px;width:46px;height:172px;background:var(--band)"></div>
  <div class="box" style="left:62px;top:52px;background:var(--green)">What we need is a template (or master) which can be varied by ourselves from case to case</div>
  <div class="tab" style="left:198px;top:46px;background:var(--green)">01</div>
  <div class="box" style="left:214px;top:83px;background:var(--plum)">What we need is a template (or master) which can be varied by ourselves from case to case</div>
  <div class="tab" style="left:166px;top:85px;background:var(--plum)">02</div>
  <div class="box" style="left:62px;top:121px;background:var(--green)">What we need is a template (or master) which can be varied by ourselves from case to case</div>
  <div class="tab" style="left:198px;top:116px;background:var(--green)">03</div>
  <div class="box" style="left:214px;top:156px;background:var(--plum)">What we need is a template (or master) which can be varied by ourselves from case to case</div>
  <div class="tab" style="left:166px;top:152px;background:var(--plum)">04</div>
  <div class="brand"><i></i>Verindale</div>
  <p class="footer-url">www.verindale.com</p>
  <span class="page-no">01</span>
</section>

<!-- Table -->
<section class="slide table-slide">
  <h2 class="slide-title">INSERT YOU SUB TITLE HERE</h2>
  <table>
    <tr><td>Insert your text here</td><td>Insert your text here</td></tr>
    <tr><td>Insert your text here</td><td>Insert your text here</td></tr>
    <tr><td>Insert your text here</td><td>Insert your text here</td></tr>
    <tr><td>Insert your text here</td><td>Insert your text here</td></tr>
    <tr><td>Insert your text here</td><td>Insert your text here</td></tr>
    <tr><td>Insert your text here</td><td>Insert your text here</td></tr>
    <tr><td>Insert your text here</td><td>Insert your text here</td></tr>
    <tr><td>Insert your text here</td><td>Insert your text here</td></tr>
    <tr><td>Insert your text here</td><td>Insert your text here</td></tr>
    <tr><td>Insert your text here</td><td>Insert your text here</td></tr>
    <tr><td>Insert your text here</td><td>Insert your text here</td></tr>
    <tr><td>Insert your text here</td><td>Insert your text here</td></tr>
  </table>
  <div class="brand"><i></i>Verindale</div>
  <p class="footer-url">www.verindale.com</p>
  <span class="page-no">01</span>
</section>

<!-- Team -->
<section class="slide team">
  <h2 class="slide-title">INSERT YOU SUB TITLE HERE</h2>
  <div class="member" style="left:24px"><div class="face" role="img" aria-label="Team member portrait"></div><h3>Name of the Member<br>Designation</h3><p>Often times, TCM rules and regulations are overlooked when the proper time and attention fails to be given to quality assurance.</p></div>
  <div class="member" style="left:103px"><div class="face" role="img" aria-label="Team member portrait"></div><h3>Name of the Member<br>Designation</h3><p>Often times, TCM rules and regulations are overlooked when the proper time and attention fails to be given to quality assurance.</p></div>
  <div class="member" style="left:183px"><div class="face" role="img" aria-label="Team member portrait"></div><h3>Name of the Member<br>Designation</h3><p>Often times, TCM rules and regulations are overlooked when the proper time and attention fails to be given to quality assurance.</p></div>
  <div class="member" style="left:264px"><div class="face" role="img" aria-label="Team member portrait"></div><h3>Name of the Member<br>Designation</h3><p>Often times, TCM rules and regulations are overlooked when the proper time and attention fails to be given to quality assurance.</p></div>
  <div class="brand"><i></i>Verindale</div>
  <p class="footer-url">www.verindale.com</p>
  <span class="page-no">01</span>
</section>

<!-- Chart -->
<section class="slide chart-slide">
  <h2 class="slide-title">INSERT YOU SUB TITLE HERE</h2>
  <svg width="378" height="130" viewBox="0 0 378 130" style="position:absolute;left:0;top:0" font-family="Open Sans,Arial,sans-serif">
    <line x1="52" y1="44" x2="52" y2="108" stroke="#bbb" stroke-width=".6"/>
    <line x1="52" y1="108" x2="338" y2="108" stroke="#bbb" stroke-width=".6"/>
    <g font-size="5" fill="#444" text-anchor="middle">
      <text x="52" y="118">0</text><text x="93" y="118">2</text><text x="134" y="118">4</text><text x="175" y="118">6</text>
      <text x="215" y="118">8</text><text x="256" y="118">10</text><text x="297" y="118">12</text><text x="338" y="118">14</text>
    </g>
    <g font-size="4.5" fill="#444" text-anchor="end">
      <text transform="translate(48 55) rotate(-40)">Category 4</text>
      <text transform="translate(48 70) rotate(-40)">Category 3</text>
      <text transform="translate(48 86) rotate(-40)">Category 2</text>
      <text transform="translate(48 100) rotate(-40)">Category 1</text>
    </g>
    <g>
      <rect x="52" y="49" width="94" height="6" fill="#8cc63f"/><rect x="146" y="49" width="55" height="6" fill="#3a3a3a"/><rect x="201" y="49" width="102" height="6" fill="#8a8a8a"/>
      <rect x="52" y="64" width="74" height="6" fill="#8cc63f"/><rect x="126" y="64" width="34" height="6" fill="#3a3a3a"/><rect x="160" y="64" width="62" height="6" fill="#8a8a8a"/>
      <rect x="52" y="79" width="51" height="6" fill="#8cc63f"/><rect x="103" y="79" width="92" height="6" fill="#3a3a3a"/><rect x="195" y="79" width="41" height="6" fill="#8a8a8a"/>
      <rect x="52" y="94" width="90" height="6" fill="#8cc63f"/><rect x="142" y="94" width="49" height="6" fill="#3a3a3a"/><rect x="191" y="94" width="41" height="6" fill="#8a8a8a"/>
    </g>
  </svg>
  <div class="legend" style="left:38px"><b><i style="background:var(--green)"></i>Insert your text here</b>What we need is a template (or master) which can be</div>
  <div class="legend" style="left:148px"><b><i style="background:var(--chart-dark)"></i>Insert your text here</b>What we need is a template (or master) which can be varied by</div>
  <div class="legend" style="left:262px"><b><i style="background:var(--chart-grey)"></i>Insert your text here</b>What we need is a template (or master) which can be varied by</div>
  <div class="brand"><i></i>Verindale</div>
  <p class="footer-url">www.verindale.com</p>
  <span class="page-no">01</span>
</section>

<!-- Columns & testimonial -->
<section class="slide quotes">
  <div class="band"></div>
  <h2 class="slide-title">INSERT YOU SUB TITLE HERE</h2>
  <div class="col" style="left:42px"><b><svg width="9" height="7" viewBox="0 0 9 7"><rect x=".5" y=".5" width="8" height="6" fill="none" stroke="#fff"/></svg>Number one</b>What we need is a template (or master) which can be varied by ourselves from case to case. Most of our cases are colorful and it's important to transport the passion of</div>
  <div class="col" style="left:150px"><b><svg width="9" height="7" viewBox="0 0 9 7"><circle cx="4.5" cy="3.5" r="3" fill="none" stroke="#fff"/></svg>Number one</b>What we need is a template (or master) which can be varied by ourselves from case to case. Most of our cases are colorful and it's important to transport the passion of</div>
  <div class="col" style="left:260px"><b><svg width="9" height="7" viewBox="0 0 9 7"><polyline points="1,6 1,1 4.5,4 8,1 8,6" fill="none" stroke="#fff"/></svg>Number one</b>What we need is a template (or master) which can be varied by ourselves from case to case. Most of our cases are colorful and it's important to transport the passion of</div>
  <p class="testimonial"><strong>Testimonials comes here</strong>“ What we need is a template (or master) which can be varied by ourselves from case to case. Most of our cases are colorful and it's important to transport the passion of”.<br><span>Followed by names of the person</span></p>
  <div class="brand"><i></i>Verindale</div>
  <p class="footer-url">www.verindale.com</p>
  <span class="page-no">01</span>
</section>

</body>
</html>
```